Visitenkarte für therapeutischen Dienstleister
Breits die ersten Designvorschläge deckten sich weitgehend mit meinem Briefing. Anfragen und Änderungen werden rasch und professionell beantwortet und umgesetzt.
Zielgruppe
siehe Briefing
Aufgabenstellung

```html
<!DOCTYPE html>
<html lang="fr">
<head>
<meta charset="utf-8">
<title>Lionel Berthoud – Carte de visite</title>
<link rel="stylesheet" href="https://fonts.googleapis.com/css2?family=Inter:ital,wght@0,300;0,400;0,600;0,700;0,800;1,300&display=swap">
<style>
  :root {
    --page-bg: #e8e8e8;
    --card-white: #ffffff;
    --sand: #c2a584;
    --sand-soft: #d9c6ae;
    --ink: #0a0a0a;
    --paper-line: #ffffff;
    --shadow: rgba(0, 0, 0, 0.28);
  }
  * { margin: 0; padding: 0; box-sizing: border-box; }
  html, body {
    width: 1200px;
    height: 2400px;
    overflow: hidden;
    background: var(--page-bg);
    font-family: "Inter", Helvetica, Arial, sans-serif;
  }
  .canvas { position: relative; width: 1200px; height: 2400px; }

  .card {
    position: absolute;
    left: 150px;
    width: 900px;
    height: 570px;
    border-radius: 34px;
    box-shadow: 6px 10px 14px var(--shadow);
    overflow: hidden;
  }
  .card--front { top: 82px; background: var(--card-white); }
  .card--back { top: 720px; background: var(--sand); color: var(--paper-line); }

  /* Front */
  .brand {
    position: absolute;
    left: 46px;
    top: 48px;
    display: flex;
    align-items: center;
    gap: 12px;
  }
  .brand__dot {
    width: 36px; height: 36px;
    border-radius: 50%;
    background: var(--sand);
  }
  .brand__name {
    font-size: 27px;
    font-weight: 600;
    color: var(--ink);
    letter-spacing: 0.5px;
  }
  .identity {
    position: absolute;
    right: 263px;
    top: 282px;
    text-align: right;
  }
  .identity__first,
  .identity__last {
    font-weight: 800;
    font-size: 108px;
    line-height: 98px;
    letter-spacing: -2px;
  }
  .identity__first { color: var(--sand); }
  .identity__last { color: var(--ink); }
  .identity__title {
    margin-top: 20px;
    font-size: 25px;
    font-weight: 300;
    font-style: italic;
    color: var(--ink);
  }
  .legs-art--front {
    position: absolute;
    right: 0; top: 0;
    width: 250px; height: 570px;
    background: linear-gradient(180deg, var(--card-white) 0%, var(--sand-soft) 45%, var(--sand) 100%);
    opacity: 0.75;
  }

  /* Back */
  .legs-art--back {
    position: absolute;
    left: 0; top: 0;
    width: 262px; height: 570px;
    background: linear-gradient(180deg, var(--sand) 0%, var(--sand-soft) 55%, #efe6da 100%);
  }
  .specialty {
    position: absolute;
    right: 84px;
    top: 60px;
    text-align: right;
    font-size: 41px;
    font-weight: 700;
    line-height: 54px;
    letter-spacing: -0.5px;
  }
  .services {
    position: absolute;
    left: 0; top: 188px;
    width: 900px; height: 180px;
  }
  .service {
    position: absolute;
    top: 0;
    width: 200px;
    margin-left: -100px;
    text-align: center;
  }
  .service__name {
    font-size: 20px;
    font-weight: 400;
    line-height: 24px;
    color: var(--paper-line);
    height: 50px;
  }
  .service__icon {
    display: block;
    margin: 12px auto 0;
    width: 110px; height: 96px;
    background: var(--ink);
    border-radius: 8px;
    opacity: 0.85;
  }
  .service--massage { left: 353px; }
  .service--pelvis { left: 572px; }
  .service--golf { left: 763px; }

  .contact {
    position: absolute;
    left: 338px; top: 377px;
    width: 478px; height: 146px;
    border: 1.5px solid var(--paper-line);
    padding: 18px 28px 0 0;
    text-align: right;
    font-size: 19px;
    font-weight: 300;
    line-height: 28px;
  }
  .contact__label { font-weight: 300; }
  .contact__line { font-weight: 400; }
</style>
</head>
<body>
<main class="canvas">

  <section class="card card--front" aria-label="Recto de la carte">
    <div class="brand">
      <span class="brand__dot"></span>
      <span class="brand__name">Relais Santé</span>
    </div>
    <div class="legs-art legs-art--front" role="img" aria-label="Silhouette de jambes en couleur sable le long du bord déchiré"></div>
    <div class="identity">
      <div class="identity__first">LIONEL</div>
      <div class="identity__last">BERTHOUD</div>
      <p class="identity__title">Masseur médical avec brevet fédéral</p>
    </div>
  </section>

  <section class="card card--back" aria-label="Verso de la carte">
    <div class="legs-art legs-art--back" role="img" aria-label="Silhouette de jambes blanches le long du bord déchiré"></div>
    <h2 class="specialty">THERAPIE MUSCULO<br>SQUELETTIQUE</h2>

    <div class="services">
      <div class="service service--massage">
        <p class="service__name">Relais<br>massage</p>
        <span class="service__icon" role="img" aria-label="Pictogramme d'un thérapeute massant un patient"></span>
      </div>
      <div class="service service--pelvis">
        <p class="service__name">Relais blocage<br>sacro-iliaque</p>
        <span class="service__icon" role="img" aria-label="Pictogramme d'un bassin et de la colonne lombaire"></span>
      </div>
      <div class="service service--golf">
        <p class="service__name">Relais golf<br>thérapie</p>
        <span class="service__icon" role="img" aria-label="Silhouette d'un golfeur tenant son club sur les épaules"></span>
      </div>
    </div>

    <address class="contact">
      <p class="contact__label">Contact:</p>
      <p class="contact__line">Chemin des Vergers 14, 1207 Genève</p>
      <p class="contact__line">www.relais-sante-exemple.ch</p>
      <p class="contact__line">079 000 12 34</p>
    </address>
  </section>

</main>
</body>
</html>
```